Business Card and Stationary Design for Solstice Land Company
Solstice Land Partners
Business Card and Stationary Design for Solstice Land Company - Real Estate
Creative Brief
Use same font as used in my logo
Tobias "TK" Kalder
Realtor
2876 Mellow Crest Lane Irvine, CA 92611
tk@TheSolsticeLP.example
www.TheSolsticeLP.example
BRE Lic: 07326159
We need the following design work done: Business Cards, Presentation Folder, Letterhead, Envelopes. We will upload our logo and the design templates from our print shop for all the above items needed in order to print correctly. Business Cards (Front & Back): 4 color both sides. Presentation Folder - (Front, Back and inside) 4 colors all sides, including business card slit inside.
We will upload pictures of sample business cards (Front and Back) that we like from competitor companies.

```html
<!DOCTYPE html>
<html lang="en">
<head>
<meta charset="utf-8">
<title>Solstice Land Partners – Business Card</title>
<link href="https://fonts.googleapis.com/css2?family=Montserrat:wght@700;800&family=Open+Sans:wght@400;600&display=swap" rel="stylesheet">
<style>
  :root {
    --backdrop: #5e5e5e;
    --card: #ffffff;
    --card-shade: #eeeeee;
    --ink: #151515;
    --accent: #f07a18;
    --muted: #6a6a6a;
    --on-dark: #ffffff;
  }
  * { box-sizing: border-box; margin: 0; padding: 0; }
  html, body { width: 1200px; height: 737px; overflow: hidden; }
  body {
    background: var(--backdrop);
    font-family: "Open Sans", Arial, sans-serif;
    position: relative;
  }
  .card {
    position: absolute;
    top: 210px;
    width: 520px;
    height: 318px;
    border-radius: 22px;
    overflow: hidden;
    background: linear-gradient(160deg, var(--card) 40%, var(--card-shade));
    box-shadow: 0 10px 24px rgba(0,0,0,.35);
  }
  .card--front { left: 55px; }
  .card--back { left: 625px; }
  .card__art { position: absolute; inset: 0; }
  .holder {
    position: absolute;
    top: 26px;
    right: 34px;
    text-align: right;
    color: var(--on-dark);
  }
  .holder__name {
    font-size: 15px;
    font-weight: 600;
    letter-spacing: 2px;
    text-transform: uppercase;
  }
  .holder__title {
    font-size: 10px;
    letter-spacing: 1px;
    margin-top: 3px;
    color: #d8d8d8;
  }
  .brand {
    position: absolute;
    display: flex;
    align-items: center;
    gap: 8px;
    font-family: "Montserrat", Arial, sans-serif;
    font-weight: 800;
    color: var(--ink);
    letter-spacing: -1px;
    text-transform: lowercase;
  }
  .brand__mark { background: var(--accent); display: block; }
  .card--front .brand { left: 32px; top: 170px; font-size: 36px; }
  .card--front .brand__mark { width: 18px; height: 18px; }
  .card--back .brand {
    left: 50%; top: 50%;
    transform: translate(-50%, -50%);
    font-size: 54px;
  }
  .card--back .brand__mark { width: 26px; height: 26px; }
  .contacts {
    position: absolute;
    left: 34px;
    top: 226px;
    list-style: none;
    font-size: 8.5px;
    line-height: 13px;
    color: var(--muted);
  }
  .contacts li { display: flex; align-items: center; gap: 6px; }
  .contacts svg { width: 8px; height: 8px; fill: var(--accent); flex: none; }
</style>
</head>
<body>
  <section class="card card--front">
    <svg class="card__art" viewBox="0 0 520 318" aria-hidden="true">
      <path d="M0 0 H520 V60 C380 95 200 120 0 160 Z" fill="#141414"/>
      <path d="M0 166 C200 126 380 101 520 66" fill="none" stroke="var(--accent)" stroke-width="5"/>
    </svg>
    <div class="holder">
      <p class="holder__name">Tobias "TK" Kalder</p>
      <p class="holder__title">Realtor</p>
    </div>
    <div class="brand">
      <span>solstice</span><span class="brand__mark"></span>
    </div>
    <ul class="contacts">
      <li><svg viewBox="0 0 10 10"><path d="M5 0a3.5 3.5 0 0 0-3.5 3.5C1.5 6 5 10 5 10s3.5-4 3.5-6.5A3.5 3.5 0 0 0 5 0z"/></svg>2876 Mellow Crest Lane Irvine, CA 92611</li>
      <li><svg viewBox="0 0 10 10"><rect x="0" y="2" width="10" height="6"/></svg>tk@TheSolsticeLP.example</li>
      <li><svg viewBox="0 0 10 10"><circle cx="5" cy="5" r="4.5"/></svg>www.TheSolsticeLP.example</li>
      <li><svg viewBox="0 0 10 10"><rect x="1" y="1" width="8" height="8" rx="1"/></svg>BRE Lic: 07326159</li>
    </ul>
  </section>

  <section class="card card--back">
    <div class="brand">
      <span>solstice</span><span class="brand__mark"></span>
    </div>
  </section>
</body>
</html>
```